Stationery Design Project

We need letterhead and business cards designed for our consulting firm. Color scheme, mostly deep blue (see logo). We are a commercial consulting work out firm, nationwide (large loans, $10MM and up). Visit our website for more info.
Updates

Project Deadline Extended
Reason: Meeting tomorrow morning to make final final decision. Would like this project to stay open to be able to provide feed back and receive final edits and approve. Thank you!!!

Target Market(s)

High end investors

Industry/Entity Type

Business

Requirements
Must have
• Letterhead must have the logo and the address

4817 Larkmoor Avenue, Suite 210, San Diego, CA 92107
Nice to have
• It would be nice to incorporate a watermark of all or some portion of the logo on the letterhead, or at least for the 2nd sheets.

Maybe our phone number: 858.555.0174
and/or webiste: www.tollandridgecap.example
Should not have
• Target users and audience of this will be men so, frilly or whimsical type designs are not preferred.

```html
<!DOCTYPE html>
<html lang="en">
<head>
<meta charset="utf-8">
<title>Tolland Ridge Capital — Business Card</title>
<link rel="stylesheet" href="https://fonts.googleapis.com/css2?family=Cinzel:wght@400&family=Roboto:wght@400;700&display=swap">
<style>
  :root {
    --page: #ecebe8;
    --card: #ffffff;
    --brand-blue: #1a7fc1;
    --brand-gray: #6d6e71;
    --text-dark: #3d3d3d;
    --wave-tint: #e3eff7;
    --faint: #eeeeee;
  }
  * { margin: 0; padding: 0; box-sizing: border-box; }
  html, body { width: 1200px; height: 441px; overflow: hidden; background: var(--page); }
  .canvas { position: relative; width: 1200px; height: 441px; }
  .card {
    position: absolute; top: 58px; width: 548px; height: 309px;
    background: var(--card);
    box-shadow: 0 2px 6px rgba(0,0,0,0.18);
    overflow: hidden;
  }
  .card--front { left: 42px; }
  .card--back { left: 616px; }

  .brand { position: absolute; left: 0; width: 370px; top: 60px; text-align: center; }
  .brand__mark { display: block; width: 22px; height: 22px; margin: 0 auto 14px; background: var(--brand-blue); }
  .brand__name {
    font-family: "Cinzel", serif; font-weight: 400; font-size: 31px; line-height: 36px;
    color: var(--brand-gray); letter-spacing: 1px;
  }

  .rule { position: absolute; top: 193px; height: 2px; background: var(--brand-blue); }
  .rule--long { left: 0; width: 355px; }
  .rule--short { left: 522px; width: 26px; }
  .holder {
    position: absolute; top: 181px; left: 366px;
    font-family: "Roboto", sans-serif; white-space: nowrap;
  }
  .holder__name { font-weight: 700; font-size: 17px; color: var(--brand-blue); }
  .holder__title { font-weight: 700; font-size: 13px; color: var(--text-dark); margin-left: 3px; }

  .contact {
    position: absolute; right: 36px; top: 225px; text-align: right;
    font-family: "Roboto", sans-serif; font-size: 12px; color: var(--text-dark);
  }
  .contact__row { height: 21px; line-height: 21px; display: flex; justify-content: flex-end; align-items: center; gap: 7px; }
  .contact__row svg { width: 12px; height: 12px; }
  .contact__row--address { margin-right: -19px; padding-top: 2px; }

  .back__name {
    position: absolute; top: 78px; left: 0; width: 100%; text-align: center;
    font-family: "Cinzel", serif; font-weight: 400; font-size: 54px; line-height: 64px;
    color: var(--faint);
  }
  .back__band { position: absolute; left: 0; top: 236px; width: 100%; height: 62px; background: var(--wave-tint); }
  .back__web {
    position: absolute; top: 268px; width: 100%; text-align: center;
    font-family: "Roboto", sans-serif; font-size: 12px; letter-spacing: 2.4px; color: var(--text-dark);
  }
  .back__web b { font-weight: 700; }
</style>
</head>
<body>
<main class="canvas">
  <section class="card card--front">
    <div class="brand">
      <span class="brand__mark"></span>
      <div class="brand__name">Tolland Ridge<br>Capital</div>
    </div>
    <div class="rule rule--long"></div>
    <div class="holder"><span class="holder__name">Your Name</span><span class="holder__title">Title</span></div>
    <div class="rule rule--short"></div>
    <div class="contact">
      <div class="contact__row">858.555.0174
        <svg viewBox="0 0 12 12" aria-hidden="true"><circle cx="6" cy="6" r="5.3" fill="none" stroke="var(--brand-blue)" stroke-width="1"/><path d="M4 3.2l1.1 1.6-.6.7c.4.8 1 1.4 1.8 1.8l.7-.6 1.6 1.1-.7 1c-2.3-.4-4.2-2.3-4.6-4.6z" fill="var(--brand-blue)"/></svg>
      </div>
      <div class="contact__row">www.tollandridgecap.example
        <svg viewBox="0 0 12 12" aria-hidden="true"><circle cx="6" cy="6" r="5" fill="none" stroke="var(--brand-blue)" stroke-width="1"/><ellipse cx="6" cy="6" rx="2.2" ry="5" fill="none" stroke="var(--brand-blue)" stroke-width="0.9"/><path d="M1 6h10M2 3.5h8M2 8.5h8" stroke="var(--brand-blue)" stroke-width="0.8"/></svg>
      </div>
      <div class="contact__row contact__row--address">4817 Larkmoor Avenue, Suite 210, San Diego, CA 92107</div>
    </div>
  </section>

  <section class="card card--back">
    <div class="back__name">Tolland Ridge<br>Capital</div>
    <div class="back__band"></div>
    <div class="back__web">www.<b>tollandridgecap</b>.example</div>
  </section>
</main>
</body>
</html>
```